PELUNO soap beauty bar

I need a box designed to put a 4oz bar of soap inside. All sides of the box need design. A refreshingly fragrant blend of citrus and spicy notes, it is made with a blend of essential oils including ginger, mandarin, lemon and orange flowers

Target Market(s)

Homeless people

Requirements
Must have
• My company logo as pictured with text and design like a standard bar of soap. Weight 4oz, ingredients:
Olive oil, Coconut oil,Organic sustainable palm oil,Water,Lye,Shea butter, orange, ginger, mandarin, lemon essential oil. uploading pics for inspiration.
Nice to have
• The soap box measurements are Dimensions (L x W x H). 5.75 x 3.80 x 5.60 Inches ...

```html
<!DOCTYPE html>
<html lang="en">
<head>
<meta charset="utf-8">
<title>PELUNO Body Soap – Box Dieline</title>
<link rel="stylesheet" href="https://fonts.googleapis.com/css2?family=Pacifico&family=Oswald:wght@600&family=Montserrat:wght@500;700;800&display=swap">
<style>
  :root{
    --green:#1f5a32;
    --green-deep:#174a29;
    --green-bright:#2f9a45;
    --lime:#d5dd2b;
    --paper:#ffffff;
    --pattern:#fbfbe9;
    --outline:#111111;
    --wood-light:#a86d3c;
    --wood-dark:#5c3a1f;
    --citrus-light:#f7c531;
    --citrus-dark:#e0902a;
    --stage:#ffffff;
    --ink:#555555;
  }
  html,body{margin:0;width:681px;height:1200px;overflow:hidden;background:var(--stage);}
  .dieline{display:block;width:681px;height:1200px;}
  .cut{stroke:var(--outline);stroke-width:1.2;stroke-linejoin:round;}
  .flap-white{fill:var(--paper);}
  .flap-green{fill:var(--green);}
  .panel-green{fill:var(--green);}
  .panel-pattern{fill:var(--pattern);}
  .label-white{fill:var(--paper);}
  .band-lime{fill:var(--lime);}
  .seam{fill:none;stroke:var(--lime);stroke-width:3;stroke-dasharray:3 3;}
  .script{font-family:'Pacifico',cursive;fill:var(--paper);}
  .tagline{font-family:'Montserrat',sans-serif;font-weight:700;fill:var(--paper);font-size:5px;letter-spacing:.3px;}
  .net{font-family:'Oswald',sans-serif;font-weight:600;fill:var(--green);font-size:7px;}
  .blend{font-family:'Oswald',sans-serif;font-weight:600;fill:var(--green-deep);font-size:10px;letter-spacing:.4px;}
  .blurb{font-family:'Montserrat',sans-serif;font-weight:500;fill:var(--ink);font-size:5.4px;}
  .ingredients{font-family:'Montserrat',sans-serif;font-weight:500;fill:var(--green-deep);font-size:6.2px;}
  .brand{font-family:'Montserrat',sans-serif;font-weight:800;fill:var(--green);}
  .brand-side{fill:var(--green-bright);}
  .brand-dot{fill:var(--green);}
  .icon-line{fill:none;stroke:var(--green);stroke-width:2;stroke-linecap:round;stroke-linejoin:round;}
</style>
</head>
<body>
<svg class="dieline" viewBox="18 236 569 792" preserveAspectRatio="xMidYMid meet" xmlns="http://www.w3.org/2000/svg" aria-label="PELUNO body soap box, flat dieline">
  <defs>
    <linearGradient id="wood" x1="0" y1="0" x2="1" y2="1">
      <stop offset="0" stop-color="#a86d3c"/>
      <stop offset="1" stop-color="#5c3a1f"/>
    </linearGradient>
    <linearGradient id="citrus" x1="0" y1="0" x2="1" y2="0">
      <stop offset="0" stop-color="#e0902a"/>
      <stop offset="1" stop-color="#f7c531"/>
    </linearGradient>
  </defs>

  <!-- top tuck flap -->
  <path class="flap-white cut" d="M143,290 L143,262 L150,262 L153,245 L452,245 L455,262 L462,262 L462,290 Z"/>

  <!-- upper side flaps -->
  <path class="flap-green cut" d="M143,300 L103,300 L103,290 L62,290 L48,302 L48,330 L25,336 L25,470 L48,476 L48,500 L143,508 Z"/>
  <path class="flap-green cut" d="M462,300 L502,300 L502,290 L543,290 L557,302 L557,330 L580,336 L580,470 L557,476 L557,500 L462,508 Z"/>

  <!-- back panel (printed upside down) -->
  <g class="panel panel-back" transform="rotate(180 302.5 398)">
    <rect class="panel-pattern" x="143" y="288" width="319" height="220"/>
    <rect class="panel-green" x="143" y="288" width="112" height="220"/>
    <line class="seam" x1="255" y1="288" x2="255" y2="508"/>
    <path class="label-white" d="M168,316 H240 V352 L204,346 L168,352 Z"/>
    <circle class="brand-dot" cx="180" cy="330" r="3.5"/>
    <text class="brand" x="187" y="333" font-size="9">PELUNO</text>
    <text class="script" x="158" y="400" font-size="26">Body</text>
    <text class="script" x="180" y="438" font-size="26">Soap</text>
    <text class="tagline" x="170" y="456">WITH NATURAL OILS</text>
    <rect class="label-white" x="162" y="488" width="78" height="13"/>
    <text class="net" x="170" y="498">NET CONTENT: 4 OZ</text>
    <rect role="img" aria-label="Photo of a dropper bottle on a wooden bowl with bay leaves" x="345" y="288" width="117" height="162" fill="url(#wood)"/>
    <rect class="band-lime" x="260" y="442" width="202" height="24"/>
    <rect role="img" aria-label="Illustration of ginger root and citrus slices" x="276" y="436" width="60" height="32" rx="10" fill="url(#citrus)"/>
    <text class="blend" x="342" y="458">CITRUS AND SPICE BLEND</text>
    <text class="blurb" x="262" y="480">Soap made with a blend of essential oils including ginger,</text>
    <text class="blurb" x="262" y="488">mandarin, lemon and orange flowers</text>
  </g>

  <!-- base panel with ingredients (printed upside down) -->
  <path class="panel-green cut" d="M65,530 H540 Q553,530 553,545 V610 Q553,625 540,625 H65 Q50,625 50,610 V545 Q50,530 65,530 Z"/>
  <g class="panel panel-base" transform="rotate(180 301.5 577.5)">
    <path class="label-white" d="M165,546 H437 L445,554 V601 L437,609 H165 L157,601 V554 Z"/>
    <path fill="none" stroke="var(--green)" stroke-width="1" d="M168,550 H434 L441,557 V598 L434,605 H168 L161,598 V557 Z"/>
    <circle class="brand-dot" cx="201" cy="568" r="6"/>
    <text class="brand" x="176" y="592" font-size="10">PELUNO</text>
    <text class="ingredients" x="252" y="566">Ingredients:</text>
    <text class="ingredients" x="252" y="575">Olive oil, Coconut oil,Organic sustainable palm</text>
    <text class="ingredients" x="252" y="584">oil,Water, Lye,Shea butter, orange, ginger,</text>
    <text class="ingredients" x="252" y="593">mandarin, lemon essential oil.</text>
  </g>

  <!-- lower side panels -->
  <path class="flap-green cut" d="M143,645 L25,652 L25,690 L38,696 L38,818 L25,824 L25,858 L143,865 Z"/>
  <path class="flap-green cut" d="M462,645 L580,652 L580,690 L567,696 L567,818 L580,824 L580,858 L462,865 Z"/>
  <g class="side-mark" transform="rotate(90 68 755)">
    <text class="brand brand-side" x="68" y="760" font-size="13" text-anchor="middle">PELUNO</text>
  </g>
  <g class="side-mark" transform="rotate(-90 537 755)">
    <text class="brand brand-side" x="537" y="760" font-size="13" text-anchor="middle">PELUNO</text>
  </g>

  <!-- front panel -->
  <g class="panel panel-front">
    <rect class="panel-pattern" x="143" y="643" width="319" height="222"/>
    <rect class="panel-green" x="143" y="643" width="110" height="222"/>
    <line class="seam" x1="253" y1="643" x2="253" y2="865"/>
    <path class="label-white" d="M155,643 H240 V703 L198,694 L155,703 Z"/>
    <circle class="brand-dot" cx="197" cy="662" r="7"/>
    <text class="brand" x="197" y="688" font-size="11" text-anchor="middle">PELUNO</text>
    <text class="script" x="152" y="752" font-size="28">Body</text>
    <text class="script" x="172" y="790" font-size="28">Soap</text>
    <text class="tagline" x="170" y="811">WITH NATURAL OILS</text>
    <rect class="label-white" x="166" y="827" width="78" height="14"/>
    <text class="net" x="173" y="837">NET CONTENT: 4 OZ</text>
    <rect class="band-lime" x="260" y="802" width="202" height="24"/>
    <rect role="img" aria-label="Illustration of ginger root and citrus slices" x="262" y="778" width="80" height="44" rx="14" fill="url(#citrus)"/>
    <text class="blend" x="344" y="818">CITRUS AND SPICE BLEND</text>
    <text class="blurb" x="262" y="836">Soap made with a blend of essential oils including ginger, mandarin,</text>
    <text class="blurb" x="262" y="845">lemon and orange flowers</text>
  </g>

  <!-- bottom flaps and panel -->
  <path class="flap-white cut" d="M143,882 L48,882 L42,900 L42,1014 L143,1014 Z"/>
  <path class="flap-white cut" d="M462,882 L557,882 L563,900 L563,1014 L462,1014 Z"/>
  <g class="panel panel-bottom">
    <rect class="panel-pattern cut" x="143" y="865" width="319" height="149"/>
    <g class="recycle-icon" aria-label="Recyclable">
      <path class="icon-line" d="M155,888 A7,7 0 1 1 160,892"/>
      <path class="icon-line" d="M155,884 L155,889 L160,889"/>
    </g>
    <circle class="brand-dot" cx="297" cy="898" r="10"/>
    <text class="brand" x="297" y="930" font-size="15" text-anchor="middle">PELUNO</text>
  </g>
</svg>
</body>
</html>
```